Intranet for company management ERP Style

We need a redesign for our Intranet webpage (Images, CSS), we have all the code and functionality ready and a basic design but it is not good looking. In order to meet our company standards this design has to be fully responsive and elegant, also should display the colors of the company: (#F17808 #EDAA64 #F4B947 #F2A900 #292828 #3D3D3D #062953) usually Dark orange colors are the main ones, though we wouldn't mind to see other options or to implement a pair of skins that we could switch easily on the webpage.

Target Market(s)

this webpage is for internal use of the company but could also be sold to external customers in the future, our market is cryptocurrency and BPO

Industry/Entity Type

BPO, Cryptocurrency

Coding

Coded - Design and coding required

Number of Pages Required

1 page

Font styles to use
Other font styles liked:
• Headings: Montserrat Extra Bold, Sub headings: Montserrat, Text: Object Sans

Colors
F0912C
F2A743
F7CA91
FBE8D2
FDF5EE

Requirements
Nice to have
• elegant icons designs and menus

```html
<!DOCTYPE html>
<html lang="en">
<head>
<meta charset="utf-8">
<title>Nodewell Intranet – Suggestion</title>
<link href="https://fonts.googleapis.com/css2?family=Montserrat:wght@500;600;700;800&family=Open+Sans:wght@400;600&display=swap" rel="stylesheet">
<style>
:root{
  --stage:#2b2a28;
  --orange:#F0912C;
  --orange-2:#F2A743;
  --peach:#F7CA91;
  --sand:#FBE8D2;
  --panel:#F0F0F0;
  --white:#ffffff;
  --ink:#3D3D3D;
  --ink-soft:#555;
  --line:#d9d9d9;
  --gear:#5b5b5b;
}
*{box-sizing:border-box;margin:0;padding:0}
html,body{width:795px;height:1200px;overflow:hidden;background:var(--stage)}
body{position:relative;font-family:"Montserrat",sans-serif;color:var(--ink)}
.screen{position:absolute;left:28px;width:738px;height:554px;background:var(--white);overflow:hidden}
.screen--form{top:23px}
.screen--report{top:607px}
.abs{position:absolute}

.topbar{left:0;top:0;width:738px;height:54px;background:var(--orange)}
.brand{left:18px;top:17px;display:flex;align-items:center;gap:6px;color:var(--white);font-weight:800;font-size:15px;letter-spacing:.2px}
.brand-dot{width:14px;height:14px;border-radius:50%;background:var(--white)}
.tool{top:21px;width:12px;height:12px;fill:var(--white)}
.round-btn{top:18px;width:19px;height:19px;border-radius:50%;background:var(--white);display:flex;align-items:center;justify-content:center}
.round-btn svg{width:9px;height:9px;fill:var(--ink)}

.sidebar{left:0;top:64px;width:129px;height:490px;background:var(--sand);border-top-right-radius:20px}
.side-foot{left:0;top:525px;width:120px;height:29px;background:linear-gradient(90deg,var(--orange-2),var(--orange));border-top-right-radius:16px;display:flex;align-items:center;justify-content:space-around;padding:0 14px 0 18px}
.side-foot svg{width:8px;height:8px;fill:var(--white)}
.nav-item{left:7px;width:122px;height:24px;display:flex;align-items:center;padding-left:14px;font-size:7.6px;font-weight:600;color:var(--ink)}
.nav-item svg{width:7px;height:7px;fill:var(--orange);margin-right:13px}
.nav-item.is-active{background:var(--white);border-radius:12px 0 0 12px}
.nav-sub{left:7px;width:122px;height:14px;display:flex;align-items:center;padding-left:14px;font-size:6.8px;font-weight:600;color:var(--ink)}
.nav-sub span.chev{width:7px;margin-right:13px;font-weight:700}
.nav-sub.is-current{color:var(--orange)}

.page-title{left:145px;top:66px;font-size:12px;font-weight:800;color:var(--ink)}
.crumb{left:145px;top:84px;font-family:"Open Sans",sans-serif;font-size:7.6px;color:var(--ink)}
.crumb a{color:var(--orange);text-decoration:none}
.counter{right:18px;top:76px;font-family:"Open Sans",sans-serif;font-size:7.6px}
.counter b{color:var(--orange);font-family:"Montserrat",sans-serif;font-weight:800}

.panel{left:145px;top:105px;width:593px;height:449px;background:var(--panel);border-top-left-radius:20px}
.panel-head{left:15px;top:12px;font-size:12px;font-weight:500;color:var(--orange)}
.panel-rule{left:0;top:36px;width:593px;height:1px;background:var(--line)}
.field-label{left:15px;font-size:8px;font-weight:500;color:var(--ink)}
.textarea{left:15px;width:560px;height:57px;background:var(--white);border-radius:5px}
.select{left:15px;top:316px;width:560px;height:27px;background:var(--white);border-radius:14px;display:flex;align-items:center;justify-content:space-between;padding:0 12px;font-size:7.6px;font-weight:500}
.select svg{width:6px;height:7px;fill:var(--ink)}
.btn-save{left:15px;top:359px;width:101px;height:28px;border-radius:14px;background:linear-gradient(180deg,var(--orange-2),var(--orange));color:var(--white);font-size:9px;font-weight:500;display:flex;align-items:center;justify-content:center}
.foot-rule{left:0;top:414px;width:593px;height:1px;background:var(--line)}
.copyright{left:15px;top:427px;font-family:"Open Sans",sans-serif;font-size:7px}
.zoom{right:6px;top:428px;font-family:"Open Sans",sans-serif;font-size:8.5px}
.fab{left:554px;top:419px;width:25px;height:25px;border-radius:50%;background:var(--gear);display:flex;align-items:center;justify-content:center}
.fab svg{width:8px;height:8px;fill:var(--white)}

.export{top:20px;height:16px;border:1px solid #cfcfcf;background:var(--white);border-radius:8px;font-size:7px;font-weight:500;display:flex;align-items:center;justify-content:center}
.search{left:437px;top:20px;width:137px;height:16px;border:1px solid #cfcfcf;background:var(--white);border-radius:8px;font-size:7px;font-weight:500;display:flex;align-items:center;justify-content:space-between;padding:0 9px}
.search svg{width:7px;height:7px;fill:var(--ink)}

.table{left:15px;top:49px;width:560px;height:281px;background:var(--white);border-radius:10px;overflow:hidden}
.thead{left:0;top:0;width:560px;height:30px;background:var(--peach)}
.th{top:10px;font-size:7.6px;font-weight:600;color:var(--ink);display:flex;align-items:center;gap:3px}
.th svg{width:4px;height:7px;fill:var(--ink)}
.row{left:0;width:560px;height:30px;border-bottom:1px solid var(--line)}
.td{top:10px;font-family:"Open Sans",sans-serif;font-size:7.6px;color:var(--ink)}
.pager{left:453px;top:251px;width:100px;height:23px;background:#ebebeb;border-radius:12px;display:flex;align-items:center;justify-content:center;gap:2px;font-size:7.6px;font-weight:600}
.pager .num{width:17px;height:17px;border-radius:50%;background:var(--orange);color:var(--white);display:flex;align-items:center;justify-content:center}
</style>
</head>
<body>
<svg width="0" height="0" style="position:absolute">
  <symbol id="i-menu" viewBox="0 0 12 12"><rect y="2" width="12" height="1.6"/><rect y="5.2" width="12" height="1.6"/><rect y="8.4" width="12" height="1.6"/></symbol>
  <symbol id="i-search" viewBox="0 0 12 12"><path d="M5 1a4 4 0 1 1 0 8 4 4 0 0 1 0-8zm0 1.6a2.4 2.4 0 1 0 0 4.8 2.4 2.4 0 0 0 0-4.8zM8 7.6l3.4 3.4-1.1 1.1L6.9 8.7z"/></symbol>
  <symbol id="i-grid" viewBox="0 0 12 12"><rect x="1" y="1" width="4.5" height="4.5"/><rect x="6.5" y="1" width="4.5" height="4.5"/><rect x="1" y="6.5" width="4.5" height="4.5"/><rect x="6.5" y="6.5" width="4.5" height="4.5"/></symbol>
  <symbol id="i-chat" viewBox="0 0 12 12"><path d="M6 1.5c3 0 5.5 1.8 5.5 4.2S9 9.9 6 9.9c-.6 0-1.2-.1-1.7-.2L1.5 11l.9-2.2C1.2 8 .5 6.9.5 5.7.5 3.3 3 1.5 6 1.5z"/></symbol>
  <symbol id="i-bell" viewBox="0 0 12 12"><path d="M6 1a3.5 3.5 0 0 1 3.5 3.5V8l1.5 1.5H1L2.5 8V4.5A3.5 3.5 0 0 1 6 1zm-1.3 9.2h2.6a1.3 1.3 0 0 1-2.6 0z"/></symbol>
  <symbol id="i-user" viewBox="0 0 12 12"><circle cx="6" cy="3.6" r="2.6"/><path d="M1 11.5c0-3 2.2-4.8 5-4.8s5 1.8 5 4.8z"/></symbol>
  <symbol id="i-gauge" viewBox="0 0 12 12"><path d="M6 2a5.5 5.5 0 0 1 5.5 5.5c0 1-.3 2-.8 2.8H1.3A5.5 5.5 0 0 1 6 2zm0 3.2L5 8.3a1 1 0 1 0 1.9.3z"/></symbol>
  <symbol id="i-alert" viewBox="0 0 12 12"><circle cx="6" cy="6" r="5.5"/><rect x="5.2" y="2.8" width="1.6" height="4" fill="#fff"/><rect x="5.2" y="7.6" width="1.6" height="1.6" fill="#fff"/></symbol>
  <symbol id="i-pie" viewBox="0 0 12 12"><path d="M5.3 1.3v5.4h5.4A5.4 5.4 0 1 1 5.3 1.3zM6.7.5a5 5 0 0 1 4.8 4.8H6.7z"/></symbol>
  <symbol id="i-talk" viewBox="0 0 12 12"><path d="M4.5 1.5c2.3 0 4.2 1.4 4.2 3.2S6.8 7.9 4.5 7.9c-.4 0-.8 0-1.2-.1L1 8.8l.6-1.6C.8 6.6.3 5.7.3 4.7c0-1.8 1.9-3.2 4.2-3.2zm5.3 3c1.2.6 1.9 1.5 1.9 2.6 0 .8-.4 1.5-1 2l.5 1.4-2-.8c-.4.1-.8.1-1.2.1-1.2 0-2.3-.4-3-1.1 2.6-.2 4.6-1.9 4.8-4.2z"/></symbol>
  <symbol id="i-dollar" viewBox="0 0 12 12"><path d="M6.7.5v1.4c1.2.2 2.1.9 2.4 2L7.6 4.4c-.2-.7-.8-1-1.6-1-.9 0-1.4.4-1.4 1 0 .6.5.8 1.8 1.2 1.7.5 2.9 1 2.9 2.6 0 1.3-1 2.2-2.6 2.4v1.4H5.4V10.5C4 10.3 3 9.5 2.7 8.2l1.6-.5c.2.9.9 1.3 1.8 1.3 1 0 1.5-.4 1.5-1 0-.7-.6-.9-1.9-1.3C4.1 6.2 3 5.7 3 4.3c0-1.2.9-2.1 2.4-2.4V.5z"/></symbol>
  <symbol id="i-doc" viewBox="0 0 12 12"><path d="M2 .5h5l3 3v8H2zm5 0v3h3z"/><rect x="3.5" y="6" width="5" height="1" fill="#fff"/><rect x="3.5" y="8" width="5" height="1" fill="#fff"/></symbol>
  <symbol id="i-shield" viewBox="0 0 12 12"><path d="M6 .5l5 2v3.2c0 3-2.1 5.2-5 5.8C3.1 10.9 1 8.7 1 5.7V2.5z"/></symbol>
  <symbol id="i-gear" viewBox="0 0 12 12"><path d="M5 .5h2l.3 1.6 1.2.6 1.4-.9 1.4 1.4-.9 1.4.6 1.2 1.6.3v2l-1.6.3-.6 1.2.9 1.4-1.4 1.4-1.4-.9-1.2.6L7 11.5H5l-.3-1.6-1.2-.6-1.4.9L.7 8.8l.9-1.4L1 6.2-.5 6V4l1.6-.3.6-1.2L.7 1.1 2.1-.3l1.4.9 1.2-.6zM6 4a2 2 0 1 0 0 4 2 2 0 0 0 0-4z"/></symbol>
  <symbol id="i-mail" viewBox="0 0 12 12"><path d="M.5 2.5h11v1.2L6 7 .5 3.7zm0 2.6L6 8.4l5.5-3.3v4.4H.5z"/></symbol>
  <symbol id="i-power" viewBox="0 0 12 12"><rect x="5.2" y=".5" width="1.6" height="5.5"/><path d="M3.2 2.2l1 1.2a3.5 3.5 0 1 0 3.6 0l1-1.2a5 5 0 1 1-5.6 0z"/></symbol>
  <symbol id="i-sort" viewBox="0 0 4 7"><path d="M2 0l2 2.8H0zM2 7L0 4.2h4z"/></symbol>
</svg>

<!-- Add suggestion screen -->
<section class="screen screen--form">
  <header class="abs topbar">
    <div class="abs brand"><span class="brand-dot"></span>Nodewell</div>
    <svg class="abs tool" style="left:170px"><use href="#i-menu"/></svg>
    <svg class="abs tool" style="left:192px"><use href="#i-search"/></svg>
    <svg class="abs tool" style="left:214px"><use href="#i-grid"/></svg>
    <div class="abs round-btn" style="left:646px"><svg><use href="#i-chat"/></svg></div>
    <div class="abs round-btn" style="left:674px"><svg><use href="#i-bell"/></svg></div>
    <div class="abs round-btn" style="left:701px"><svg><use href="#i-user"/></svg></div>
  </header>

  <nav class="abs sidebar">
    <div class="abs nav-item" style="top:25px"><svg><use href="#i-gauge"/></svg>Home</div>
    <div class="abs nav-item" style="top:55px"><svg><use href="#i-alert"/></svg>Request</div>
    <div class="abs nav-item" style="top:84px"><svg><use href="#i-pie"/></svg>Reports</div>
    <div class="abs nav-item" style="top:114px"><svg><use href="#i-talk"/></svg>Helpdesk</div>
    <div class="abs nav-item" style="top:143px"><svg><use href="#i-dollar"/></svg>Payroll</div>
    <div class="abs nav-item is-active" style="top:173px"><svg><use href="#i-doc"/></svg>Suggestion Box</div>
    <div class="abs nav-item" style="top:202px"><svg><use href="#i-shield"/></svg>Administrator</div>
  </nav>
  <div class="abs side-foot"><svg><use href="#i-gear"/></svg><svg><use href="#i-mail"/></svg><svg><use href="#i-power"/></svg></div>

  <h1 class="abs page-title">Suggestion</h1>
  <p class="abs crumb"><a href="#">Home</a> / Add New suggestion</p>

  <main class="abs panel">
    <h2 class="abs panel-head">Add New Suggestion</h2>
    <div class="abs panel-rule"></div>
    <label class="abs field-label" style="top:46px">Describe your suggestion</label>
    <div class="abs textarea" style="top:63px"></div>
    <label class="abs field-label" style="top:130px">How would your suggestion help us?</label>
    <div class="abs textarea" style="top:147px"></div>
    <label class="abs field-label" style="top:213px">Additional Comment</label>
    <div class="abs textarea" style="top:231px"></div>
    <label class="abs field-label" style="top:298px">Country</label>
    <div class="abs select">Select<svg><use href="#i-sort"/></svg></div>
    <div class="abs btn-save">Save</div>
    <div class="abs foot-rule"></div>
    <p class="abs copyright">© 2022. Nodewell</p>
    <span class="abs zoom">x10</span>
  </main>
</section>

<!-- Suggestion report screen -->
<section class="screen screen--report">
  <header class="abs topbar">
    <div class="abs brand"><span class="brand-dot"></span>Nodewell</div>
    <svg class="abs tool" style="left:170px"><use href="#i-menu"/></svg>
    <svg class="abs tool" style="left:192px"><use href="#i-search"/></svg>
    <svg class="abs tool" style="left:214px"><use href="#i-grid"/></svg>
    <div class="abs round-btn" style="left:646px"><svg><use href="#i-chat"/></svg></div>
    <div class="abs round-btn" style="left:674px"><svg><use href="#i-bell"/></svg></div>
    <div class="abs round-btn" style="left:701px"><svg><use href="#i-user"/></svg></div>
  </header>

  <nav class="abs sidebar">
    <div class="abs nav-item" style="top:25px"><svg><use href="#i-gauge"/></svg>Home</div>
    <div class="abs nav-item" style="top:55px"><svg><use href="#i-alert"/></svg>Request</div>
    <div class="abs nav-item is-active" style="top:84px"><svg><use href="#i-pie"/></svg>Reports</div>
    <div class="abs nav-sub" style="top:117px"><span class="chev">»</span>Policy</div>
    <div class="abs nav-sub is-current" style="top:135px"><span class="chev">»</span>Suggestion Dashboard</div>
    <div class="abs nav-item" style="top:159px"><svg><use href="#i-talk"/></svg>Helpdesk</div>
    <div class="abs nav-item" style="top:189px"><svg><use href="#i-dollar"/></svg>Payroll</div>
    <div class="abs nav-item" style="top:218px"><svg><use href="#i-doc"/></svg>Suggestion Box</div>
    <div class="abs nav-item" style="top:248px"><svg><use href="#i-shield"/></svg>Administrator</div>
  </nav>
  <div class="abs side-foot"><svg><use href="#i-gear"/></svg><svg><use href="#i-mail"/></svg><svg><use href="#i-power"/></svg></div>

  <h1 class="abs page-title">Suggestion</h1>
  <p class="abs crumb"><a href="#">Report</a> / Suggestion</p>
  <p class="abs counter">Suggestion Number: <b>4</b></p>

  <main class="abs panel">
    <div class="abs export" style="left:15px;width:41px">Copy</div>
    <div class="abs export" style="left:59px;width:42px">CSV</div>
    <div class="abs export" style="left:104px;width:41px">Excel</div>
    <div class="abs export" style="left:149px;width:41px">PDF</div>
    <div class="abs export" style="left:193px;width:42px">Print</div>
    <div class="abs search">Search<svg><use href="#i-search"/></svg></div>

    <div class="abs table">
      <div class="abs thead">
        <div class="abs th" style="left:11px">Username<svg><use href="#i-sort"/></svg></div>
        <div class="abs th" style="left:126px">Description<svg><use href="#i-sort"/></svg></div>
        <div class="abs th" style="left:234px">Suggestion Help<svg><use href="#i-sort"/></svg></div>
        <div class="abs th" style="left:351px">Comments<svg><use href="#i-sort"/></svg></div>
        <div class="abs th" style="left:440px">Date<svg><use href="#i-sort"/></svg></div>
      </div>
      <div class="abs row" style="top:31px"><span class="abs td" style="left:11px">Super Admin</span><span class="abs td" style="left:126px">Hola</span><span class="abs td" style="left:234px">Hola</span><span class="abs td" style="left:351px">Test</span><span class="abs td" style="left:440px">Jan 20, 2022 08:48AM</span></div>
      <div class="abs row" style="top:62px"><span class="abs td" style="left:11px">Super Admin</span><span class="abs td" style="left:126px">Hola</span><span class="abs td" style="left:234px">Hola</span><span class="abs td" style="left:351px">Test</span><span class="abs td" style="left:440px">Jan 20, 2022 08:48AM</span></div>
      <div class="abs row" style="top:92px"><span class="abs td" style="left:11px">Super Admin</span><span class="abs td" style="left:126px">Hola</span><span class="abs td" style="left:234px">Hola</span><span class="abs td" style="left:351px">Test</span><span class="abs td" style="left:440px">Jan 20, 2022 08:48AM</span></div>
      <div class="abs row" style="top:122px"><span class="abs td" style="left:11px">Super Admin</span><span class="abs td" style="left:126px">Hola</span><span class="abs td" style="left:234px">Hola</span><span class="abs td" style="left:351px">Test</span><span class="abs td" style="left:440px">Jan 20, 2022 08:48AM</span></div>
      <div class="abs row" style="top:152px"><span class="abs td" style="left:11px">Super Admin</span><span class="abs td" style="left:126px">Hola</span><span class="abs td" style="left:234px">Hola</span><span class="abs td" style="left:351px">Test</span><span class="abs td" style="left:440px">Jan 20, 2022 08:48AM</span></div>
      <div class="abs row" style="top:181px"><span class="abs td" style="left:11px">Super Admin</span><span class="abs td" style="left:126px">Hola</span><span class="abs td" style="left:234px">Hola</span><span class="abs td" style="left:351px">Test</span><span class="abs td" style="left:440px">Jan 20, 2022 08:48AM</span></div>
      <div class="abs row" style="top:212px"><span class="abs td" style="left:11px">Super Admin</span><span class="abs td" style="left:126px">Hola</span><span class="abs td" style="left:234px">Hola</span><span class="abs td" style="left:351px">Test</span><span class="abs td" style="left:440px">Jan 20, 2022 08:48AM</span></div>
      <div class="abs pager">Previous <span class="num">1</span> Next</div>
    </div>

    <div class="abs foot-rule"></div>
    <p class="abs copyright">© 2022. Nodewell</p>
    <div class="abs fab"><svg><use href="#i-gear"/></svg></div>
    <span class="abs zoom">x10</span>
  </main>
</section>
</body>
</html>
```